Business Card for a Floral & Decorating Business

I would like to take my current logo and create a better business card. I am looking for elegance as I am a florist and event decorator. My logo has multiple colour options. I like colours like green, purple, pink and orange, I think I would like a white card, open to black back ground. I want it to feel elegant and romantic. I like metallic lettering that maybe is indented in the paper, I also like glossy paper. I have a full logo already as well as a badge. I have attached both in multiple colours.m
Updates

Need extra days to review

Target Market(s)

Weddings, special events, floral customers

Industry/Entity Type

Floral and decorating

Contact Information for Business Card

Phone number, email, instagram, facebook, title, name, logo

Font styles to use
Script

Requirements
Nice to have
• Elegant

```html
<!DOCTYPE html>
<html lang="en">
<head>
<meta charset="utf-8">
<title>Marlowe Ainsley – Decorating &amp; Florals Business Card</title>
<link rel="stylesheet" href="https://fonts.googleapis.com/css2?family=Bodoni+Moda:wght@400&family=Dancing+Script:wght@500&display=swap">
<style>
  :root {
    --backdrop: #e4e4e2;
    --paper: #ffffff;
    --plum: #9b3366;
    --monogram: #a0425a;
    --rose: #cf468e;
    --ink: #1b1b1b;
  }
  * { margin: 0; padding: 0; box-sizing: border-box; }
  html, body { width: 1200px; height: 846px; overflow: hidden; background: var(--backdrop); }
  .canvas { position: relative; width: 1200px; height: 846px; }
  .card { position: absolute; left: 346px; width: 508px; height: 290px; overflow: hidden; }
  .card--front { top: 99px; background: var(--paper); }
  .card--back { top: 456px; background: var(--plum); }

  .monogram-area {
    position: absolute; left: 0; top: 0; width: 140px; height: 290px;
    background: linear-gradient(90deg, var(--monogram) 0%, #b86a82 55%, rgba(255,255,255,0) 100%);
  }

  .identity { position: absolute; left: 211px; top: 52px; }
  .identity__name {
    font-family: "Dancing Script", cursive; font-weight: 500;
    font-size: 36px; line-height: 1; color: var(--plum);
  }
  .identity__title {
    font-family: "Dancing Script", cursive; font-weight: 500;
    font-size: 23px; line-height: 1; color: var(--ink); margin-top: 6px;
  }

  .contact-list { position: absolute; left: 186px; top: 149px; list-style: none; }
  .contact-list__item {
    display: flex; align-items: center; height: 24.3px;
    font-family: "Bodoni Moda", serif; font-size: 16.5px;
    letter-spacing: 0.6px; color: var(--ink);
  }
  .contact-list__icon { width: 18px; height: 18px; margin-right: 10px; flex: none; }

  .wordmark {
    position: absolute; left: 0; right: 0; text-align: center;
  }
  .wordmark__mark {
    position: absolute; left: 234px; top: 60px; width: 40px; height: 40px;
    border-radius: 50%; background: var(--rose);
  }
  .wordmark__name {
    position: absolute; left: 0; right: 0; top: 150px; text-align: center;
    font-family: "Bodoni Moda", serif; font-size: 44px; font-weight: 400;
    color: var(--rose); letter-spacing: 1px;
  }
  .wordmark__tagline {
    position: absolute; left: 0; right: 0; top: 228px; text-align: center;
    padding-left: 60px;
    font-family: "Bodoni Moda", serif; font-size: 11px;
    letter-spacing: 6px; color: var(--rose);
  }
</style>
</head>
<body>
<main class="canvas">

  <section class="card card--front">
    <div class="monogram-area" role="img" aria-label="Floral monogram decoration"></div>

    <div class="identity">
      <h1 class="identity__name">Marlowe Ainsley</h1>
      <p class="identity__title">Decorating &amp; Florals</p>
    </div>

    <ul class="contact-list">
      <li class="contact-list__item">
        <svg class="contact-list__icon" viewBox="0 0 24 24" aria-hidden="true">
          <path fill="#9b3366" d="M6.6 2.5c.8-.4 1.7-.1 2.1.7l1.3 2.9c.3.7.1 1.5-.5 1.9l-1.3.9c.7 3.4 2.3 6.6 4.6 9l1.5-.5c.7-.2 1.5 0 1.9.7l1.5 2.6c.4.8.2 1.7-.6 2.1l-1.7.9c-1.2.6-2.7.4-3.7-.6C6.9 18.4 4.3 12.1 4.6 5.6c.1-1.2.8-2.3 1.9-2.8z"/>
        </svg>
        +1 555-013-4827
      </li>
      <li class="contact-list__item">
        <svg class="contact-list__icon" viewBox="0 0 24 24" aria-hidden="true">
          <rect x="1" y="5" width="22" height="14" rx="1" fill="#9b3366"/>
          <path d="M2 6l10 7 10-7" fill="none" stroke="#ffffff" stroke-width="1.8"/>
        </svg>
        MarloweAinsley@mailnest.com
      </li>
      <li class="contact-list__item">
        <svg class="contact-list__icon" viewBox="0 0 24 24" aria-hidden="true">
          <rect x="4" y="4" width="16" height="16" fill="#9b3366"/>
        </svg>
        blossomandbanquetdecorating
      </li>
      <li class="contact-list__item">
        <svg class="contact-list__icon" viewBox="0 0 24 24" aria-hidden="true">
          <circle cx="12" cy="12" r="8" fill="#9b3366"/>
        </svg>
        marloweainsleydecorating.florals
      </li>
    </ul>
  </section>

  <section class="card card--back">
    <div class="wordmark__mark"></div>
    <p class="wordmark__name">Marlowe Ainsley</p>
    <p class="wordmark__tagline">DECORATING &amp; FLORALS.</p>
  </section>

</main>
</body>
</html>
```